Beard Balm Label

Hi Chaps,

We are needing a label for a new product we are adding to our international beard grooming range.

The design needs to be on a circular label. There will be a top label (that will contain the branding and what the product is) and a bottom label (that will contain the instructions for use and ingredients).

The size of the top label is 75mm in diameter.

The size of the bottom label is 68mm in diameter

It needs to align with our branding from our Beard Oil and Moustache wax product. checkout www.thegrizzledgent.com to get an insight of this.

What needs to be on the label:

- The grizzled gent logo (logo attached)
- Hearthside Beard Balm
- the words "Quality Craftsmanship" "Handmade in Australia" "Protect, Condition, Style"
- "Our all natural Hearthside Beard Balm is made in ABSURDLY small batches and will help you keep even the wildest beard looking sharp, lush and smelling great."
-TheGrizzledGent.com

*all fonts are attached

Information on the bottom label is not important at this stage and will provide the detail after a winner has been chosen.

This project will be open for 5 days.

Any questions, please ask asap.

```html
<!DOCTYPE html>
<html lang="en">
<head>
<meta charset="utf-8">
<title>Hearthside Beard Balm — Top Label</title>
<link rel="stylesheet" href="https://fonts.googleapis.com/css2?family=Francois+One&family=Inter:wght@500&display=swap">
<style>
  :root {
    --page: #ffffff;
    --ink: #231f20;
    --cream: #efeeb9;
  }
  html, body {
    margin: 0;
    padding: 0;
    width: 1200px;
    height: 1000px;
    overflow: hidden;
    background: var(--page);
  }
  .label-canvas {
    position: relative;
    width: 1200px;
    height: 1000px;
  }
  .label-art {
    position: absolute;
    inset: 0;
  }
  .arc-title {
    font-family: "Francois One", "Arial Narrow", sans-serif;
    font-size: 34px;
    letter-spacing: 2px;
    fill: var(--ink);
    text-transform: uppercase;
  }
  .arc-values {
    font-family: "Francois One", "Arial Narrow", sans-serif;
    font-size: 20px;
    letter-spacing: 1px;
    fill: var(--ink);
  }
  .brand-name {
    font-family: "Francois One", "Arial Narrow", sans-serif;
    font-size: 40px;
    fill: var(--ink);
    text-transform: uppercase;
  }
  .product-blurb {
    position: absolute;
    left: 452px;
    top: 548px;
    width: 282px;
    margin: 0;
    font-family: "Inter", Helvetica, Arial, sans-serif;
    font-weight: 500;
    font-size: 12.4px;
    line-height: 15.4px;
    text-align: center;
    text-transform: uppercase;
    color: var(--ink);
  }
  .blurb-rule {
    position: absolute;
    left: 501px;
    top: 628px;
    width: 183px;
    height: 3px;
    background: var(--ink);
  }
  .site-url {
    position: absolute;
    left: 452px;
    top: 638px;
    width: 282px;
    margin: 0;
    font-family: "Francois One", "Arial Narrow", sans-serif;
    font-size: 14px;
    letter-spacing: 0.6px;
    text-align: center;
    text-transform: uppercase;
    color: var(--ink);
  }
</style>
</head>
<body>
<main class="label-canvas">
  <svg class="label-art" width="1200" height="1000" viewBox="0 0 1200 1000" xmlns="http://www.w3.org/2000/svg">
    <defs>
      <path id="title-arc" d="M 392 470 A 200 200 0 0 1 792 470"/>
      <path id="values-arc" d="M 391 376 A 222 222 0 1 0 793 376"/>
    </defs>

    <circle class="label-rim" cx="592" cy="470" r="266" fill="var(--ink)"/>
    <circle class="label-face" cx="592" cy="470" r="255" fill="var(--cream)"/>
    <circle class="label-stitch" cx="592" cy="470" r="245" fill="none" stroke="var(--ink)" stroke-width="2" stroke-dasharray="5 4"/>

    <text class="arc-title">
      <textPath href="#title-arc" startOffset="50%" text-anchor="middle">Hearthside Beard Balm</textPath>
    </text>

    <text class="arc-values">
      <textPath href="#values-arc" startOffset="50%" text-anchor="middle">Quality Craftsmanship • Handmade in Australia • Protect, Condition, Style</textPath>
    </text>

    <g class="brand-mark">
      <circle cx="592" cy="412" r="96" fill="none" stroke="var(--ink)" stroke-width="3"/>
      <text class="brand-name" x="592" y="400" text-anchor="middle">The Grizzled</text>
      <text class="brand-name" x="592" y="446" text-anchor="middle">Gent</text>
    </g>
  </svg>

  <p class="product-blurb">Our all natural Hearthside Beard Balm is made in absurdly small batches and will help you keep even the wildest beard looking sharp, lush and smelling great.</p>
  <div class="blurb-rule"></div>
  <p class="site-url">TheGrizzledGent.com</p>
</main>
</body>
</html>
```